Realtor resource

This is a website that provides resources for Realtors and their customers (home buyers and sellers).

There are 5 pages that I need redesigned:

1. Homepage: https://brightkeyguide.example/
2. Support Page/Contact Us: https://brightkeyguide.example/contact-us/
3. Agent Dashboard - See attached screenshot
4. Real Estate Documents page - See attached screenshot
5. Real Estate Contract page - see attached screenshot

Target Market(s)

Real estate agents and their customers.

Industry/Entity Type

Real Estate

Number of Pages Required

5+ page

Requirements
Must have
• Please use a modern design and incorporate design with current logo.

```html
<!DOCTYPE html>
<html lang="en">
<head>
<meta charset="utf-8">
<title>BrightKey Guide – Real Estate Contracts Explained</title>
<link href="https://fonts.googleapis.com/css2?family=Lato:ital,wght@0,400;0,700;0,900;1,400&family=Josefin+Sans:wght@700&family=Varela+Round&display=swap" rel="stylesheet">
<style>
:root{
  --blue:#0a84e0;
  --blue-deep:#0d5fa6;
  --blue-hero:#0b6fc4;
  --orange:#f7941d;
  --white:#ffffff;
  --grey-text:#7d7d7d;
  --grey-dark:#555555;
  --grey-light:#f3f3f3;
  --footer:#1d1d1d;
  --footer-bar:#121212;
  --footer-text:#9a9a9a;
}
*{box-sizing:border-box;margin:0;padding:0}
html,body{width:1200px;height:3270px;overflow:hidden}
body{position:relative;font-family:"Lato",sans-serif;background:var(--white);color:var(--grey-dark)}
.abs{position:absolute}
/* header + hero */
.hero{left:0;top:0;width:1200px;height:634px;background:linear-gradient(180deg,#0a72cc 0%,#0b6cbf 45%,#0d4f8f 100%)}
.brand{left:46px;top:29px;display:flex;align-items:center;gap:8px;font-weight:700;font-size:26px;color:var(--white)}
.brand-dot{width:26px;height:26px;border-radius:50%;background:var(--orange)}
.nav{top:34px;font-size:16px;color:var(--white);letter-spacing:.3px}
.hero-arrow{top:292px}
.hero-title{left:174px;top:262px;font-weight:700;font-size:32px;line-height:50px;color:var(--white)}
.hero-text{left:174px;top:380px;width:720px;font-size:17px;line-height:34px;color:var(--white)}
.btn-orange{left:174px;top:480px;width:180px;height:38px;background:var(--orange);color:var(--white);font-size:15px;font-weight:700;letter-spacing:.8px;display:flex;align-items:center;justify-content:center}
/* login choice */
.choice-title{left:114px;top:748px;font-family:"Josefin Sans",sans-serif;font-size:38px;line-height:66px;letter-spacing:3px;color:var(--orange)}
.choice-sub{left:114px;top:878px;font-family:"Varela Round",sans-serif;font-size:33px;letter-spacing:1.5px;color:var(--grey-text)}
.choice-text{left:114px;top:932px;width:540px;font-family:"Varela Round",sans-serif;font-size:19px;line-height:34px;letter-spacing:1px;color:#9a9a9a}
.btn-choice{left:736px;width:334px;height:74px;background:var(--blue);color:var(--white);font-family:"Varela Round",sans-serif;font-size:29px;letter-spacing:2px;display:flex;align-items:center;justify-content:center}
.band{left:0;width:1200px;height:23px;background:#f0f0f0}
/* about */
.about{left:0;top:1127px;width:721px;height:494px;background:var(--blue)}
.about-photo{left:721px;top:1127px;width:479px;height:494px;background:linear-gradient(120deg,#2f7474 0%,#4a8780 45%,#9b6a3a 80%,#6d4a2b 100%)}
.about-h{font-weight:700;font-size:17px;color:var(--white)}
.about-p{width:300px;font-size:13px;line-height:25.5px;font-weight:700;color:var(--white)}
.btn-outline{left:69px;top:1501px;width:197px;height:38px;border:2px solid var(--white);color:var(--white);font-size:15px;font-weight:700;letter-spacing:.6px;display:flex;align-items:center;justify-content:center}
.big-title{left:418px;top:1215px;font-weight:900;font-size:46px;line-height:60px;letter-spacing:1px;color:var(--white)}
.big-title span{color:var(--orange)}
/* team */
.team-title{left:0;top:1700px;width:1160px;text-align:center;font-family:"Varela Round",sans-serif;font-size:40px;letter-spacing:2px;color:#5e5e5e}
.team-sub{left:190px;top:1766px;width:780px;text-align:center;font-family:"Varela Round",sans-serif;font-size:21px;line-height:34px;letter-spacing:.8px;color:var(--grey-text)}
.card{top:1881px;width:318px;height:347px}
.card-name{left:24px;bottom:44px;font-family:"Varela Round",sans-serif;font-size:17px;color:var(--white)}
.card-role{left:24px;bottom:26px;font-size:13px;color:#eeeeee}
.card-overlay{left:0;top:193px;width:318px;height:154px;background:var(--orange)}
.card-overlay p{position:absolute;left:22px;top:16px;width:280px;font-size:10.5px;line-height:18.5px;color:var(--white)}
.btn-ghost{left:505px;top:2281px;width:175px;height:47px;border:2px solid #555;font-size:14px;letter-spacing:.6px;color:#555;display:flex;align-items:center;justify-content:center}
/* testimonial */
.testimonial{left:0;top:2390px;width:1200px;height:368px;background:var(--grey-light)}
.quote{left:240px;top:2447px;width:700px;text-align:center;font-family:"Varela Round",sans-serif;font-style:italic;font-size:21px;line-height:34px;letter-spacing:.6px;color:#666;transform:skewX(-8deg)}
.avatar{left:462px;top:2608px;width:62px;height:62px;border-radius:50%;background:linear-gradient(160deg,#8fa87a,#c9a983)}
.t-name{left:546px;top:2612px;font-family:"Varela Round",sans-serif;font-size:22px;color:#333}
.t-role{left:543px;top:2645px;font-family:"Varela Round",sans-serif;font-size:17px;color:#8a8a8a}
.dot{top:2706px;width:10px;height:10px;border-radius:50%;background:#bbbbbb}
.dot.on{background:var(--blue)}
/* partners */
.partner{top:2782px;height:50px;border-radius:6px;background:#d8dde3}
/* footer */
.footer{left:0;top:2858px;width:1200px;height:372px;background:var(--footer)}
.f-h{top:2930px;font-size:17px;font-weight:700;color:var(--white)}
.f-text{font-size:14px;line-height:34px;color:var(--footer-text)}
.email{left:96px;top:3040px;width:291px;height:47px;background:var(--white);border:2px solid var(--white)}
.email span{position:absolute;left:24px;top:12px;font-size:15px;color:#b5b5b5}
.email b{position:absolute;right:0;top:0;width:48px;height:43px;background:var(--orange);color:var(--white);font-size:15px;display:flex;align-items:center;justify-content:center}
.social{top:3119px;width:44px;height:44px;border-radius:50%}
.bar{left:0;top:3230px;width:1200px;height:40px;background:var(--footer-bar)}
.bar-text{top:3242px;font-size:14px;color:var(--footer-text)}
</style>
</head>
<body>

<section class="abs hero" aria-label="Hero"></section>
<div class="abs brand"><span class="brand-dot"></span>BrightKey Guide</div>
<nav>
  <span class="abs nav" style="left:690px">SUPPORT</span>
  <span class="abs nav" style="left:800px">DOCUMENTS</span>
  <span class="abs nav" style="left:942px">LOG IN</span>
  <svg class="abs" style="left:1036px;top:34px" width="24" height="24" viewBox="0 0 24 24" fill="none" stroke="#fff" stroke-width="2.4"><circle cx="10" cy="10" r="7"/><path d="M15 15l7 7"/></svg>
  <svg class="abs" style="left:1118px;top:34px" width="38" height="24" viewBox="0 0 38 24" stroke="#fff" stroke-width="3"><path d="M2 3h34M10 12h26M2 21h34"/></svg>
</nav>
<svg class="abs hero-arrow" style="left:44px" width="26" height="40" viewBox="0 0 26 40" fill="none" stroke="#fff" stroke-width="4"><path d="M20 4L6 20l14 16"/></svg>
<svg class="abs hero-arrow" style="left:1128px" width="26" height="40" viewBox="0 0 26 40" fill="none" stroke="#fff" stroke-width="4"><path d="M6 4l14 16L6 36"/></svg>
<h1 class="abs hero-title">Real Estate Contracts Explained in plain language<br>by Texas real estate attorneys</h1>
<p class="abs hero-text">Lorem ipsum dolor sit amet, consectetur adipiscing elit. Morbi ac diam eu neque venenatis eleifend. Mauris ut quam vel enim tempus sollicitudin</p>
<a class="abs btn-orange">LEARN MORE</a>

<h2 class="abs choice-title">ARE YOU A REALTOR OR<br>BUYER/SELLER</h2>
<p class="abs choice-sub">Login by selecting your option</p>
<p class="abs choice-text">Lorem ipsum dolor sit amet, consectetur adipiscing elit. Sed accumsan erat porttitor, fermentum purus</p>
<a class="abs btn-choice" style="top:762px">REALTOR</a>
<a class="abs btn-choice" style="top:909px">BUYER/SELLER</a>
<div class="abs band" style="top:1104px"></div>

<section class="abs about" aria-label="About"></section>
<h3 class="abs about-h" style="left:64px;top:1221px">LOREM IPSUM DOLOR SIT AMET</h3>
<p class="abs about-p" style="left:64px;top:1252px">Lorem ipsum dolor sit amet, consectetur adipiscing elit. Morbi ac diam eu neque venenatis eleifend. Mauris ut quam vel enim tempus sollicitudin.</p>
<h3 class="abs about-h" style="left:64px;top:1368px">LOREM IPSUM DOLOR SIT AMET</h3>
<p class="abs about-p" style="left:64px;top:1399px">Lorem ipsum dolor sit amet, consectetur adipiscing elit. Morbi ac diam eu neque venenatis eleifend. Mauris ut quam vel enim tempus sollicitudin.</p>
<a class="abs btn-outline">LEARN MORE</a>
<h2 class="abs big-title">BRIGHTKEY<br><span>GUIDE</span></h2>
<h3 class="abs about-h" style="left:420px;top:1372px">ABOUT US</h3>
<p class="abs about-p" style="left:420px;top:1407px;width:275px">Lorem ipsum dolor sit amet, consectetur adipiscing elit. Morbi ac diam eu neque venenatis eleifend. Mauris ut quam vel enim tempus sollicitudin. Vivamus pharetra lacus eget commodo molestie. Praesent</p>
<div class="abs about-photo" role="img" aria-label="Photo of an agent and a client talking in armchairs beside a small side table with a plant"></div>
<div class="abs band" style="top:1621px"></div>

<h2 class="abs team-title" style="left:20px">Meet The Team</h2>
<p class="abs team-sub">Lorem ipsum dolor sit amet, consectetur adipiscing elit. Morbi ac diam eu neque venenatis eleifend</p>
<div class="abs card" style="left:91px;background:linear-gradient(160deg,#3c4b59,#6b5a4f 60%,#2e2c2d)" role="img" aria-label="Portrait of team manager">
  <span class="abs card-name">Dana Whitfield</span><span class="abs card-role">Manager</span>
</div>
<div class="abs card" style="left:434px;background:linear-gradient(90deg,#6a3b27,#a4684a 40%,#2b2b30 60%,#8a5237)" role="img" aria-label="Portrait of team realtor">
  <span class="abs card-name">Marcus Lee</span><span class="abs card-role">Realtor</span>
</div>
<div class="abs card" style="left:777px;background:linear-gradient(180deg,#e9e9e9,#cfcac6)" role="img" aria-label="Portrait of team manager">
  <div class="abs card-overlay"><p>Lorem ipsum dolor sit amet, consectetur adipiscing elit. Morbi pretium mauris ut ligula tempus finibus. Pellentesque malesuada est lorem, a congue ligula</p></div>
  <span class="abs card-name" style="left:22px">Robert Hale</span><span class="abs card-role" style="left:22px">Manager</span>
</div>
<a class="abs btn-ghost">MORE ABOUT US</a>

<section class="abs testimonial" aria-label="Testimonial"></section>
<svg class="abs" style="left:160px;top:2507px" width="26" height="42" viewBox="0 0 26 42" fill="none" stroke="#999" stroke-width="5"><path d="M21 4L6 21l15 17"/></svg>
<svg class="abs" style="left:980px;top:2507px" width="26" height="42" viewBox="0 0 26 42" fill="none" stroke="#999" stroke-width="5"><path d="M5 4l15 17L5 38"/></svg>
<p class="abs quote">Lorem ipsum dolor sit amet, consectetur adipiscing elit. Morbi pretium mauris ut ligula tempus finibus. Pellentesque malesuada est lorem, a congue ligula ullamcorper non. Nullam facilisis purus ante, at imperdiet nunc iaculis a. Nunc tortor augue, viverra at est a,</p>
<div class="abs avatar" role="img" aria-label="Client portrait"></div>
<span class="abs t-name">Evan Carter</span>
<span class="abs t-role">Founder at Carter Homes</span>
<span class="abs dot" style="left:570px"></span>
<span class="abs dot on" style="left:592px"></span>
<span class="abs dot" style="left:615px"></span>

<div class="abs partner" style="left:118px;width:120px" aria-label="Partner badge"></div>
<div class="abs partner" style="left:307px;width:60px" aria-label="Partner badge"></div>
<div class="abs partner" style="left:456px;width:136px" aria-label="Partner badge"></div>
<div class="abs partner" style="left:682px;width:140px" aria-label="Partner badge"></div>
<div class="abs partner" style="left:905px;width:130px" aria-label="Partner badge"></div>

<footer class="abs footer"></footer>
<h4 class="abs f-h" style="left:94px">STAY CONNECTED</h4>
<p class="abs f-text" style="left:96px;top:2956px;width:290px;color:#c8c8c8">Lorem ipsum dolor sit amet, consectetur adipiscing elit.</p>
<div class="abs email"><span>Your Email address</span><b>GO</b></div>
<span class="abs social" style="left:109px;background:#3b5998"></span>
<span class="abs social" style="left:181px;background:#1da1f2"></span>
<span class="abs social" style="left:255px;background:#4f7fa6"></span>
<span class="abs social" style="left:327px;background:#dd4b39"></span>
<h4 class="abs f-h" style="left:498px">ABOUT BRIGHTKEY</h4>
<p class="abs f-text" style="left:496px;top:2967px;width:320px">Lorem ipsum dolor sit amet, consectetur adipiscing elit. Morbi pretium mauris ut ligula tempus finibus. Pellentesque malesuada est lorem, a congue ligula ullamcorper non. Nullam</p>
<h4 class="abs f-h" style="left:886px">USEFUL LINKS</h4>
<ul class="abs f-text" style="left:887px;top:2967px;list-style:none">
  <li>Documents</li><li>FAQs</li><li>Contact</li><li>Terms and Conditions</li>
</ul>
<div class="abs bar"></div>
<span class="abs bar-text" style="left:207px">© Copyright 2019. All Rights Reserved</span>
<span class="abs bar-text" style="left:639px">Sitemap</span>
<span class="abs bar-text" style="left:748px">Privacy Policy</span>

</body>
</html>
```